Packaging designed for both the bar and the box for retail and online sales

The name of the product is Plume Crumb. We manufacture a consumer package good product that's a healthy edible cookie dough bar. The product look, feels and tastes like cookie dough. It's sold in the refrigerator section of retail stores next to cookie dough and tundra loaf. The product is Gluten Free, Diary Free and include B-12, Biotin and Collagen. The ingredients are natural. When design this think about who eat cookie dough and how to engage the buyer in purchasing the product.

We needs design packaging designed for both the bar and the box. I have attached the die lines for both products.

Target Market(s)

Our customer is 16-45. Primarily female but really anyone. Middle to upper income. Interest include healthy life style and yoga. Like to eat something sweet but not feel guilty.

Colors

Designer to choose colors to be used in the design.

Requirements
Must have
• Must be clean, warm, inviting. Brand designs I really like are Tundra Loaf.
Should not have
• Should not have a photo of food

```html
<!DOCTYPE html>
<html lang="en">
<head>
<meta charset="utf-8">
<title>Plume Crumb – Bar Wrapper Colourways</title>
<link rel="stylesheet" href="https://fonts.googleapis.com/css2?family=Oswald:wght@400;500;600&family=Mr+Dafoe&display=swap">
<style>
  :root{
    --stage:#2c2e3a;
    --paper:#f6f7f8;
    --ink-light:#ffffff;
    --dough-light:#f1dca4;
    --dough-mid:#dcb46e;
    --bowl:#8a5a44;
    --brown:#2a160e; --orange:#e8620f; --orange-badge:#f07d12; --orange-pill:#f5922a;
    --forest:#17662a; --green:#3ea83a; --green-badge:#1f7f2f; --green-pill:#1e7a2e;
    --plum:#5a1a6d; --violet:#9a3a9e; --violet-badge:#b85cb8; --violet-pill:#b455b4;
    --navy:#17509a; --blue:#1f6fbd; --blue-badge:#1b4d87;
    --petrol:#134b5f; --teal:#2cb4bf; --teal-badge:#134b5f;
    --crimson:#a7110f; --gold:#f3c10f; --red-badge:#b3141b;
  }
  *{box-sizing:border-box;margin:0;padding:0}
  html,body{width:1200px;height:1200px;overflow:hidden;background:var(--stage)}
  .stage{position:relative;width:1200px;height:1200px}

  .pack{position:absolute;width:243px;height:521px;font-family:'Oswald',sans-serif}
  .pack__body{position:absolute;left:10px;right:10px;top:0;bottom:0;background:var(--paper)}
  .pack__top{position:absolute;left:0;right:0;top:0;height:105px;background:var(--top);
    clip-path:polygon(0 0,100% 0,100% 40%,96% 100%,4% 100%,0 40%)}
  .pack__crimp{position:absolute;left:0;right:0;height:12px;
    background:repeating-linear-gradient(90deg,rgba(0,0,0,.28) 0 2px,transparent 2px 4px),var(--crimp)}
  .pack__crimp--top{top:0}
  .pack__crimp--bottom{bottom:0;height:38px}
  .pack__tag{position:absolute;top:64px;left:0;right:0;text-align:center;color:var(--ink-light);font-size:11px;letter-spacing:1.5px}
  .pack__tag span{border-top:1px solid #fff;border-bottom:1px solid #fff;padding:0 2px}

  .pack__name{position:absolute;left:46px;top:122px;font-weight:600;font-size:38px;line-height:42px;color:var(--name)}
  .pack__name span{display:block}
  .pack__name span+span{padding-left:32px}
  .pack__script{position:absolute;font-family:'Mr Dafoe',cursive;font-size:17px;line-height:20px;color:var(--name);white-space:nowrap}
  .pack__photo{position:absolute}

  .pack__band{position:absolute;left:0;right:0;background:var(--band);border-radius:50% 50% 0 0 / 22px 22px 0 0}
  .badges{position:absolute;left:0;right:0;display:flex;justify-content:center;gap:12px}
  .badge{display:flex;flex-direction:column;align-items:center;justify-content:center;color:var(--ink-light);font-size:17px;line-height:19px;font-weight:500;background:var(--badge)}
  .badge b{font-weight:500;letter-spacing:3px}
  .badge--round{width:70px;height:70px;border-radius:50%}
  .badge--square{width:70px;height:56px;border-radius:4px}
  .pills{position:absolute;left:0;right:0;display:flex;justify-content:center;gap:4px}
  .pill{background:var(--pill);color:var(--ink-light);font-size:14px;line-height:20px;padding:0 4px;border-radius:3px}
  .pack__net{position:absolute;left:0;right:0;text-align:center;font-size:12px;line-height:16px;letter-spacing:1.2px;font-weight:500;color:var(--net)}

  .theme-choc{--top:var(--brown);--crimp:#c2480a;--name:#c2480a;--band:var(--orange);--badge:var(--orange-badge);--pill:var(--orange-pill);--net:var(--brown)}
  .theme-mint{--top:var(--forest);--crimp:var(--green-badge);--name:var(--forest);--band:var(--green);--badge:var(--green-badge);--pill:var(--green-pill);--net:var(--forest)}
  .theme-berry{--top:var(--plum);--crimp:#7b1f86;--name:#7b1f86;--band:var(--violet);--badge:var(--violet-badge);--pill:var(--violet-pill);--net:var(--plum)}
  .theme-ocean{--top:var(--navy);--crimp:var(--blue);--name:#144f92;--band:var(--blue);--badge:var(--blue-badge);--pill:var(--blue-badge);--net:#ffffff;--netband:#1a5ea8}
  .theme-lagoon{--top:var(--petrol);--crimp:#26a3ad;--name:var(--petrol);--band:var(--teal);--badge:var(--teal-badge);--pill:var(--teal-badge);--net:#ffffff;--netband:var(--petrol)}
  .theme-cherry{--top:var(--crimson);--crimp:#e0a90c;--name:var(--crimson);--band:var(--gold);--badge:var(--red-badge);--pill:var(--red-badge);--net:var(--gold);--netband:var(--crimson)}

  /* round-badge wrappers */
  .pack--round .pack__script{left:76px;top:230px}
  .pack--round .pack__photo{left:58px;top:256px;width:128px;height:100px;border-radius:50% 50% 18% 18%;
    background:radial-gradient(circle at 45% 40%,var(--dough-light),var(--dough-mid))}
  .pack--round .pack__band{top:350px;height:115px}
  .pack--round .badges{top:360px}
  .pack--round .pills{top:432px}
  .pack--round .pack__net{top:468px}

  /* square-badge wrappers */
  .pack--square .pack__script{left:104px;top:228px}
  .pack--square .pack__sub{position:absolute;left:104px;top:250px;font-size:11px;line-height:14px;color:var(--name);white-space:nowrap}
  .pack--square .pack__photo--bowl{left:10px;top:218px;width:84px;height:122px;border-radius:6px 40% 40% 6px;
    background:linear-gradient(180deg,var(--dough-light) 0 35%,var(--bowl) 35%)}
  .pack--square .pack__photo--cookies{left:62px;top:280px;width:124px;height:68px;border-radius:40px;
    background:radial-gradient(ellipse at 50% 40%,var(--dough-light),var(--dough-mid))}
  .pack--square .pack__band{top:348px;height:112px}
  .pack--square .badges{top:362px}
  .pack--square .pills{top:427px}
  .pack--square .pack__netband{position:absolute;left:0;right:0;top:458px;height:30px;background:var(--netband)}
  .pack--square .pack__net{top:465px}
</style>
</head>
<body>
<main class="stage">

  <article class="pack pack--round theme-choc" style="left:133px;top:53px">
    <div class="pack__body"></div>
    <div class="pack__top"></div><div class="pack__crimp pack__crimp--top"></div>
    <p class="pack__tag"><span>NATURAL INGREDIENTS</span></p>
    <h2 class="pack__name"><span>Plume</span><span>Crumb</span></h2>
    <p class="pack__script">Healthy Edible</p>
    <div class="pack__photo" role="img" aria-label="Scoop of chocolate chip cookie dough"></div>
    <div class="pack__band"></div>
    <div class="badges"><div class="badge badge--round">GLUTEN<b>FREE</b></div><div class="badge badge--round">DIARY<b>FREE</b></div></div>
    <div class="pills"><span class="pill">COLLAGEN</span><span class="pill">BIOTIN</span><span class="pill">B-12</span></div>
    <p class="pack__net">NET WT.23 OZ(5G)</p>
    <div class="pack__crimp pack__crimp--bottom"></div>
  </article>

  <article class="pack pack--round theme-mint" style="left:480px;top:53px">
    <div class="pack__body"></div>
    <div class="pack__top"></div><div class="pack__crimp pack__crimp--top"></div>
    <p class="pack__tag"><span>NATURAL INGREDIENTS</span></p>
    <h2 class="pack__name"><span>Plume</span><span>Crumb</span></h2>
    <p class="pack__script">Healthy Edible</p>
    <div class="pack__photo" role="img" aria-label="Scoop of chocolate chip cookie dough"></div>
    <div class="pack__band"></div>
    <div class="badges"><div class="badge badge--round">GLUTEN<b>FREE</b></div><div class="badge badge--round">DIARY<b>FREE</b></div></div>
    <div class="pills"><span class="pill">COLLAGEN</span><span class="pill">BIOTIN</span><span class="pill">B-12</span></div>
    <p class="pack__net">NET WT.23 OZ(5G)</p>
    <div class="pack__crimp pack__crimp--bottom"></div>
  </article>

  <article class="pack pack--round theme-berry" style="left:843px;top:53px">
    <div class="pack__body"></div>
    <div class="pack__top"></div><div class="pack__crimp pack__crimp--top"></div>
    <p class="pack__tag"><span>NATURAL INGREDIENTS</span></p>
    <h2 class="pack__name"><span>Plume</span><span>Crumb</span></h2>
    <p class="pack__script">Healthy Edible</p>
    <div class="pack__photo" role="img" aria-label="Scoop of chocolate chip cookie dough"></div>
    <div class="pack__band"></div>
    <div class="badges"><div class="badge badge--round">GLUTEN<b>FREE</b></div><div class="badge badge--round">DIARY<b>FREE</b></div></div>
    <div class="pills"><span class="pill">COLLAGEN</span><span class="pill">BIOTIN</span><span class="pill">B-12</span></div>
    <p class="pack__net">NET WT.23 OZ(5G)</p>
    <div class="pack__crimp pack__crimp--bottom"></div>
  </article>

  <article class="pack pack--square theme-ocean" style="left:133px;top:620px">
    <div class="pack__body"></div>
    <div class="pack__top"></div><div class="pack__crimp pack__crimp--top"></div>
    <h2 class="pack__name"><span>Plume</span><span>Crumb</span></h2>
    <div class="pack__photo pack__photo--bowl" role="img" aria-label="Bowl of cookie dough"></div>
    <div class="pack__photo pack__photo--cookies" role="img" aria-label="Chocolate chip cookie dough rounds"></div>
    <p class="pack__script">Healthy Edible</p>
    <p class="pack__sub">NATURAL INGREDIENTS</p>
    <div class="pack__band"></div>
    <div class="badges"><div class="badge badge--square">GLUTEN<b>FREE</b></div><div class="badge badge--square">DIARY<b>FREE</b></div></div>
    <div class="pills"><span class="pill">COLLAGEN</span><span class="pill">BIOTIN</span><span class="pill">B-12</span></div>
    <div class="pack__netband"></div>
    <p class="pack__net">NET WT.23 OZ(5G)</p>
    <div class="pack__crimp pack__crimp--bottom"></div>
  </article>

  <article class="pack pack--square theme-lagoon" style="left:480px;top:620px">
    <div class="pack__body"></div>
    <div class="pack__top"></div><div class="pack__crimp pack__crimp--top"></div>
    <h2 class="pack__name"><span>Plume</span><span>Crumb</span></h2>
    <div class="pack__photo pack__photo--bowl" role="img" aria-label="Bowl of cookie dough"></div>
    <div class="pack__photo pack__photo--cookies" role="img" aria-label="Chocolate chip cookie dough rounds"></div>
    <p class="pack__script">Healthy Edible</p>
    <p class="pack__sub">NATURAL INGREDIENTS</p>
    <div class="pack__band"></div>
    <div class="badges"><div class="badge badge--square">GLUTEN<b>FREE</b></div><div class="badge badge--square">DIARY<b>FREE</b></div></div>
    <div class="pills"><span class="pill">COLLAGEN</span><span class="pill">BIOTIN</span><span class="pill">B-12</span></div>
    <div class="pack__netband"></div>
    <p class="pack__net">NET WT.23 OZ(5G)</p>
    <div class="pack__crimp pack__crimp--bottom"></div>
  </article>

  <article class="pack pack--square theme-cherry" style="left:843px;top:620px">
    <div class="pack__body"></div>
    <div class="pack__top"></div><div class="pack__crimp pack__crimp--top"></div>
    <h2 class="pack__name"><span>Plume</span><span>Crumb</span></h2>
    <div class="pack__photo pack__photo--bowl" role="img" aria-label="Bowl of cookie dough"></div>
    <div class="pack__photo pack__photo--cookies" role="img" aria-label="Chocolate chip cookie dough rounds"></div>
    <p class="pack__script">Healthy Edible</p>
    <p class="pack__sub">NATURAL INGREDIENTS</p>
    <div class="pack__band"></div>
    <div class="badges"><div class="badge badge--square">GLUTEN<b>FREE</b></div><div class="badge badge--square">DIARY<b>FREE</b></div></div>
    <div class="pills"><span class="pill">COLLAGEN</span><span class="pill">BIOTIN</span><span class="pill">B-12</span></div>
    <div class="pack__netband"></div>
    <p class="pack__net">NET WT.23 OZ(5G)</p>
    <div class="pack__crimp pack__crimp--bottom"></div>
  </article>

</main>
</body>
</html>
```